Engineering group involved with fire safety needs a business card

We need a business card design for a company based in Greece called "Varotis Group". We are engineers and specialized technicians, operating the following : a) Fire fighting equipment trade b) Installation , Inspection & Maintenance of fire extinguishers and fire protection systems c) Occupational Health & Safety (Risk assessment & management/ Staff training). We need a clear and simple card design. I uploaded a draft I made, in order to give you an idea of the company and how I currently imagine the design of the card. I also uploaded the logo in .png file format. We are always open to different, new suggestions and ideas you may want to submit.
Target Market(s)
industries, companies, managers, retail clients
Industry/Entity Type
Fire Safety
Contact Information for Business Card
Addresses & phone numbers (headquarters + branch), logo, name (you can find all the details on the uploaded files!)
Colors
Designer to choose colors to be used in the design.
Look and feel
Each slider illustrates characteristics of the customer's brand and the style your logo design should communicate.

```html
<!DOCTYPE html>
<html lang="en">
<head>
<meta charset="UTF-8">
<title>Varotis Group – Business Card</title>
<link href="https://fonts.googleapis.com/css2?family=Montserrat:wght@600;800&family=Open+Sans:wght@400;600&display=swap" rel="stylesheet">
<style>
  :root {
    --bg: #c9c9c9;
    --card-dark: #2f3335;
    --card-dark-2: #3a3f41;
    --card-light: #ffffff;
    --red: #c8161d;
    --ink: #2a2a2a;
    --ink-soft: #6a6a6a;
    --white: #ffffff;
  }
  * { margin: 0; padding: 0; box-sizing: border-box; }
  html, body { width: 1200px; height: 914px; overflow: hidden; }
  body {
    background: var(--bg);
    font-family: "Open Sans", Arial, sans-serif;
    position: relative;
  }
  .card {
    position: absolute;
    top: 179px;
    width: 360px;
    height: 556px;
    box-shadow: 0 10px 30px rgba(0,0,0,.22);
  }
  .card--back { left: 200px; background: var(--card-light); }
  .card--front {
    left: 640px;
    background: linear-gradient(160deg, var(--card-dark-2) 0%, var(--card-dark) 60%);
    color: var(--white);
    text-align: center;
  }
  .brand-name {
    font-family: "Montserrat", Arial, sans-serif;
    font-weight: 800;
    color: var(--red);
    letter-spacing: 1px;
    line-height: 1.05;
  }
  .card--back .brand-name {
    position: absolute; top: 58px; left: 0; right: 0;
    text-align: center; font-size: 30px;
  }
  .contact-list {
    position: absolute; top: 170px; left: 40px; right: 30px;
    list-style: none;
  }
  .contact-list li {
    display: flex; align-items: center; gap: 12px;
    font-size: 13px; color: var(--ink-soft);
    margin-bottom: 17px;
  }
  .contact-list li.is-strong { color: var(--ink); font-weight: 600; }
  .contact-list svg { flex: 0 0 20px; width: 20px; height: 20px; }
  .card--front .brand-name {
    position: absolute; top: 92px; left: 0; right: 0;
    font-size: 40px;
  }
  .person {
    position: absolute; top: 232px; left: 0; right: 0;
  }
  .person__name {
    font-family: "Montserrat", Arial, sans-serif;
    font-weight: 800; color: var(--red);
    font-size: 15px; letter-spacing: .5px;
  }
  .person__role { font-size: 13px; margin-top: 6px; }
  .services {
    position: absolute; top: 380px; left: 0; right: 0;
    list-style: none;
    font-family: "Montserrat", Arial, sans-serif;
    font-weight: 800; font-size: 13.5px; line-height: 1.85;
    text-transform: uppercase;
  }
</style>
</head>
<body>

<section class="card card--back" aria-label="Card back">
  <div class="brand-name">VAROTIS<br>GROUP</div>
  <ul class="contact-list">
    <li class="is-strong">
      <svg viewBox="0 0 20 20"><circle cx="10" cy="10" r="9" fill="#2a2a2a"/><path d="M10 4.5a3.5 3.5 0 0 0-3.5 3.5c0 2.6 3.5 7 3.5 7s3.5-4.4 3.5-7A3.5 3.5 0 0 0 10 4.5z" fill="#fff"/><circle cx="10" cy="8" r="1.3" fill="#2a2a2a"/></svg>
      <span>HQ.: 12 Ermou Str., 19005 Nea Makri<br>BO: 30 Kifisias Ave, 15124 Marousi</span>
    </li>
    <li>
      <svg viewBox="0 0 20 20"><circle cx="10" cy="10" r="9" fill="#2a2a2a"/><rect x="5.5" y="8" width="9" height="6" rx="1" fill="#fff"/><path d="M5 8c1-3 9-3 10 0" stroke="#fff" stroke-width="1.6" fill="none"/></svg>
      <span>HQ.: +30 22940 31826</span>
    </li>
    <li>
      <svg viewBox="0 0 20 20"><circle cx="10" cy="10" r="9" fill="#2a2a2a"/><rect x="5.5" y="8" width="9" height="6" rx="1" fill="#fff"/><path d="M5 8c1-3 9-3 10 0" stroke="#fff" stroke-width="1.6" fill="none"/></svg>
      <span>BO: +30 210 6124875</span>
    </li>
    <li>
      <svg viewBox="0 0 20 20"><circle cx="10" cy="10" r="9" fill="#2a2a2a"/><rect x="7" y="4.5" width="6" height="11" rx="1" fill="#fff"/><circle cx="10" cy="13.5" r=".8" fill="#2a2a2a"/></svg>
      <span>Mob.: +30 694 512 73 28</span>
    </li>
    <li>
      <svg viewBox="0 0 20 20"><circle cx="10" cy="10" r="9" fill="#2a2a2a"/><circle cx="10" cy="10" r="5" stroke="#fff" stroke-width="1.2" fill="none"/><ellipse cx="10" cy="10" rx="2" ry="5" stroke="#fff" stroke-width="1.2" fill="none"/><line x1="5" y1="10" x2="15" y2="10" stroke="#fff" stroke-width="1.2"/></svg>
      <span>www.varotisgroup.gr</span>
    </li>
    <li>
      <svg viewBox="0 0 20 20"><circle cx="10" cy="10" r="9" fill="#2a2a2a"/><rect x="5" y="6.5" width="10" height="7" rx="1" fill="#fff"/><path d="M5 7l5 4 5-4" stroke="#2a2a2a" stroke-width="1.1" fill="none"/></svg>
      <span>info@varotisgroup.gr</span>
    </li>
  </ul>
</section>

<section class="card card--front" aria-label="Card front">
  <div class="brand-name">VAROTIS<br>GROUP</div>
  <div class="person">
    <div class="person__name">NIKOS VAROTIS</div>
    <div class="person__role">Mechanical Engineer - OHS Consultant</div>
  </div>
  <ul class="services">
    <li>Fire Fighting Equipment</li>
    <li>Licensing &amp; Business Registration</li>
    <li>Occupational Health &amp; Safety</li>
    <li>Staff Training</li>
  </ul>
</section>

</body>
</html>
```